Design personal page for IT Expert

I'm freelancer in the area of IT Architecture/Cloud Computing/DevOps. <br/>Already have own page: www.brevantu.cc<br/><br/>I want to update/redesign it and have following sections/pages there:<br/>1) My short bio/details/soft skills<br/>2) List of my hard skills<br/>3) My key clients/success stories/feedbacks<br/>4) List of my conference talks with links/embedded youtube video<br/>5) List of my articles with links (probably article text on sub-page like blog)<br/><br/>Design should be compatible with wix.com (gona have premium plan there)<br/>

Number of Pages Required

4 page

Font styles to use
Sans Serif

Colors

Designer to choose colors to be used in the design.

Requirements
Must have
• 1) My short bio/details/soft skills
• 2) List of my hard skills
• 3) My key clients/success stories/feedbacks
• 4) List of my conference talks with links/embedded youtube video
• 5) List of my articles with links (probably article text on sub-page like blog)
Should not have
• No direct contact to my skype/email. I prefer to use this platform for my task discussion.

```html
<!DOCTYPE html>
<html lang="en">
<head>
<meta charset="utf-8">
<title>Marek Dovlin — Cloud DevOps &amp; Architect</title>
<link href="https://fonts.googleapis.com/css2?family=Playfair+Display:wght@700;800&family=Poppins:wght@400;500;600;700&display=swap" rel="stylesheet">
<style>
:root{
  --red:#e8391d;
  --navy:#0e1f3d;
  --ink:#1c1c1c;
  --text:#6b6b6b;
  --muted:#8a8a8a;
  --sky:#1aa3e8;
  --green:#74c64a;
  --grey-bg:#f1f1f1;
  --footer:#1e1e1e;
  --white:#ffffff;
}
*{margin:0;padding:0;box-sizing:border-box}
html,body{width:1200px;height:3926px;overflow:hidden;background:var(--white)}
body{font-family:'Poppins',sans-serif;color:var(--text)}
.page{position:relative;width:1200px;height:3926px;overflow:hidden}
.abs{position:absolute}
.serif{font-family:'Playfair Display',serif;font-weight:700;color:var(--ink)}
.btn{position:absolute;display:flex;align-items:center;justify-content:center;gap:10px;color:var(--white);font-size:12px;border-radius:3px;font-weight:500;white-space:nowrap}
.btn svg{width:15px;height:15px;flex:none}
.dot{width:13px;height:13px;border:2px solid currentColor;border-radius:50%;flex:none}
.hero-bg{position:absolute;left:0;top:0;width:1200px;height:570px}
.logo{position:absolute;font-size:26px;font-weight:500;color:var(--white);letter-spacing:.2px}
.contact{position:absolute;top:64px;display:flex;align-items:center;gap:10px;color:var(--white);font-size:13px;white-space:nowrap}
.contact svg{width:15px;height:15px}
.hero-title{position:absolute;left:0;width:1200px;top:222px;text-align:center;font-size:58px;color:var(--white)}
.hero-sub{position:absolute;left:0;width:1200px;top:308px;text-align:center;font-size:14px;color:var(--white)}
.pill{position:absolute;background:var(--red);color:var(--white);border-radius:30px;display:flex;align-items:center;justify-content:center;font-weight:600}
.menu-lines span{position:absolute;height:2px;background:var(--white);opacity:.85}
.about-p{position:absolute;left:537px;width:470px;font-size:12.5px;line-height:24px}
.skill{position:absolute;display:flex;align-items:center;gap:14px;font-size:12.5px;line-height:24px;width:330px}
.skill svg{width:30px;height:30px;flex:none}
.section-title{position:absolute;left:0;width:1200px;text-align:center;font-size:32px}
.card{position:absolute;top:1880px;width:211px;height:267px;background:var(--white);box-shadow:0 4px 10px rgba(0,0,0,.08);text-align:center;padding:0 16px}
.card .icon{width:52px;height:52px;margin:26px auto 20px;border-radius:8px}
.card h3{font-size:14px;font-weight:600;color:var(--ink);margin-bottom:10px}
.card p{font-size:12px;line-height:21.5px;color:var(--muted);word-break:break-word}
.arrow{position:absolute;top:2021px;width:38px;height:38px;border-radius:50%;background:var(--white);box-shadow:0 2px 8px rgba(0,0,0,.15);display:flex;align-items:center;justify-content:center}
.blog-img{position:absolute;top:3222px;width:280px;height:177px;border-radius:8px}
.blog h4{position:absolute;top:3422px;font-size:12.5px;font-weight:600;color:var(--ink)}
.blog p{position:absolute;top:3450px;width:260px;font-size:12px;line-height:21px;color:var(--muted)}
</style>
</head>
<body>
<svg width="0" height="0" style="position:absolute">
  <defs>
    <linearGradient id="tickGrad" x1="0" y1="0" x2="1" y2="1">
      <stop offset="0" stop-color="#f2563c"/><stop offset="1" stop-color="#d52a10"/>
    </linearGradient>
    <symbol id="tick" viewBox="0 0 30 30">
      <circle cx="15" cy="15" r="15" fill="url(#tickGrad)"/>
      <path d="M9 15.5l4 4 8-9" fill="none" stroke="#fff" stroke-width="2.6" stroke-linecap="round" stroke-linejoin="round"/>
    </symbol>
    <symbol id="download" viewBox="0 0 16 16">
      <path d="M8 2v8M4.5 7L8 10.5 11.5 7M2 11v3h12v-3" fill="none" stroke="currentColor" stroke-width="1.5" stroke-linecap="round" stroke-linejoin="round"/>
    </symbol>
    <symbol id="mail" viewBox="0 0 16 16">
      <rect x="1.5" y="3" width="13" height="10" rx="1.5" fill="none" stroke="currentColor" stroke-width="1.4"/>
      <path d="M2 4l6 5 6-5" fill="none" stroke="currentColor" stroke-width="1.4"/>
    </symbol>
    <symbol id="send" viewBox="0 0 16 16">
      <path d="M14.5 1.5L1.5 7l5 2 2 5z M6.5 9l8-7.5" fill="none" stroke="currentColor" stroke-width="1.4" stroke-linejoin="round"/>
    </symbol>
  </defs>
</svg>

<main class="page">

  <header class="hero">
    <svg class="hero-bg" viewBox="0 0 1200 570" role="img" aria-label="Portrait photograph of the consultant smiling, darkened behind the headline">
      <defs>
        <linearGradient id="heroPhoto" x1="0" y1="0" x2="1" y2="1">
          <stop offset="0" stop-color="#2b2a27"/>
          <stop offset=".5" stop-color="#3b352e"/>
          <stop offset="1" stop-color="#1d1c1a"/>
        </linearGradient>
      </defs>
      <path d="M0 0H1000C1060 240 900 560 600 565C300 568 100 480 0 365Z" fill="url(#heroPhoto)"/>
      <path d="M1000 0H1200V345C1080 500 860 572 600 565C900 560 1060 240 1000 0Z" fill="var(--red)"/>
    </svg>
    <div class="logo" style="left:155px;top:52px">Marekdovlin</div>
    <div class="contact" style="left:610px"><span class="dot"></span>Start a chat</div>
    <div class="contact" style="left:747px"><svg><use href="#mail"/></svg>Send a request</div>
    <div class="pill" style="left:915px;top:55px;width:140px;height:33px;font-size:11.5px;font-weight:700">DOWNLOAD CV</div>
    <h1 class="hero-title serif">I am Marek Dovlin</h1>
    <p class="hero-sub">NWS Cloud DevOps &amp; Architect - CI/CD Automation Expert</p>
    <div class="pill" style="left:508px;top:354px;width:174px;height:44px;font-size:14px">HIRE ME..!</div>
    <div class="menu-lines">
      <span style="left:980px;top:282px;width:48px"></span>
      <span style="left:980px;top:296px;width:48px"></span>
      <span style="left:980px;top:312px;width:48px"></span>
    </div>
  </header>

  <section class="about">
    <div class="abs" role="img" aria-label="Cut-out photograph of the consultant standing in a white shirt with a grey sweater over his shoulders" style="left:150px;top:598px;width:330px;height:507px;border-radius:160px 160px 0 0;background:linear-gradient(180deg,#e9e5e1 0%,#d9dde3 55%,#c8ccd3 100%)"></div>
    <div class="abs" style="left:470px;top:660px;width:22px;height:20px;border-radius:50%;background:#eeeeee"></div>
    <div class="abs" style="left:784px;top:658px;width:22px;height:18px;border-radius:50%;background:#eeeeee"></div>
    <div class="abs" style="left:1062px;top:726px;width:46px;height:46px;border-radius:8px;background:#f2f2f2"></div>
    <div class="abs" style="left:1030px;top:876px;width:60px;height:56px;border-radius:8px;background:#f4f4f4"></div>
    <h2 class="abs serif" style="left:537px;top:652px;font-size:25px">About Me</h2>
    <p class="about-p" style="top:705px">Lorem ipsum dolor sit amet, consectetur adipiscing elit, sed do eiusmod tempor incididunt ut labore et dolore magna aliqua.</p>
    <p class="about-p" style="top:766px">Meet my startup design agency Formline Currently I am working at Codewell as Product Designer. Before that I've worked at Brightfen, Dhaka as a UX, UI Designer. I love to work in User Experience &amp; User Interface designing. Because I love to solve the design problem and find easy and better solutions to solve it.</p>
    <div class="btn" style="left:537px;top:916px;width:155px;height:37px;background:var(--navy);font-size:11px"><svg><use href="#download"/></svg>DOWNLOAD CV</div>
    <div class="btn" style="left:705px;top:916px;width:155px;height:37px;background:var(--sky)"><svg><use href="#send"/></svg>Start a chat</div>
    <div class="btn" style="left:872px;top:916px;width:180px;height:37px;background:var(--red)"><svg><use href="#mail"/></svg>Send a request</div>
    <div class="btn" style="left:537px;top:971px;width:155px;height:37px;background:var(--sky)"><span class="dot"></span>Start a chat</div>
    <div class="btn" style="left:705px;top:971px;width:155px;height:37px;background:var(--green)"><span class="dot"></span>marekdovlin</div>
  </section>

  <section class="soft abs" style="left:0;top:1105px;width:1200px;height:626px;background:var(--grey-bg)"></section>
  <h2 class="section-title serif" style="top:1148px">Soft Skills</h2>

  <div class="skill" style="left:157px;top:1223px"><svg><use href="#tick"/></svg>Design and implementation of infrastruc-<br>ture solutions of any complexity – 16+ years</div>
  <div class="skill" style="left:157px;top:1303px"><svg><use href="#tick"/></svg>Clouds-practitioner – all cloud providers<br>in the world</div>
  <div class="skill" style="left:157px;top:1374px"><svg><use href="#tick"/></svg>Orkestra-practitioner: development,<br>implementation and training</div>
  <div class="skill" style="left:157px;top:1443px"><svg><use href="#tick"/></svg>Implementation of full cycle CI/CD<br>practices</div>
  <div class="skill" style="left:157px;top:1522px"><svg><use href="#tick"/></svg>Information security of IT-systems</div>
  <div class="skill" style="left:157px;top:1573px"><svg><use href="#tick"/></svg>Implementation of cost-effective<br>IT-solutions</div>
  <div class="skill" style="left:157px;top:1640px"><svg><use href="#tick"/></svg>Business continuity management</div>

  <div class="skill" style="left:761px;top:1223px"><svg><use href="#tick"/></svg>Introduction of modern frameworks, tools<br>and technologies</div>
  <div class="skill" style="left:761px;top:1316px"><svg><use href="#tick"/></svg>Agile practices: Scrum, Kanban</div>
  <div class="skill" style="left:761px;top:1374px"><svg><use href="#tick"/></svg>Manage cross-functional and remote<br>teams of up to 50 people</div>
  <div class="skill" style="left:761px;top:1443px"><svg><use href="#tick"/></svg>Speaker of Russian and international<br>DevOps conferences</div>
  <div class="skill" style="left:761px;top:1522px"><svg><use href="#tick"/></svg>30 + projects on Gigwise</div>
  <div class="skill" style="left:761px;top:1573px"><svg><use href="#tick"/></svg>7500 + hours Remote work: Gigwise, Free-<br>lance, DevTutor, Direct Contracts</div>
  <div class="skill" style="left:761px;top:1640px"><svg><use href="#tick"/></svg>English (including technical) – C2</div>

  <div class="abs" style="left:511px;top:1232px;width:198px;height:202px;background:var(--navy);text-align:center;color:var(--white)">
    <div style="font-size:42px;font-weight:700;margin-top:40px;line-height:46px">16+</div>
    <div style="font-size:22px;font-weight:600;line-height:28px">Years</div>
    <div style="font-size:11px;line-height:24px;margin-top:12px">Design and implementation of<br>infrastructure solutions</div>
  </div>
  <div class="abs" role="img" aria-label="Photograph of a young engineer with headphones working at a laptop" style="left:511px;top:1478px;width:198px;height:186px;background:linear-gradient(135deg,#c9c4bc 0%,#8d8a86 45%,#4d4c4c 100%)"></div>

  <section class="abs" style="left:0;top:1731px;width:1200px;height:309px;background:var(--red)"></section>
  <h2 class="section-title serif" style="top:1785px;color:var(--white)">Technical Skills</h2>

  <div class="card" style="left:146px"><div class="icon" role="img" aria-label="Illustrated icon of cloud servers" style="background:linear-gradient(135deg,#cfe3f2,#9bb8cf)"></div><h3>Cloud Providers</h3><p>Nimbara Web Services, Orlet Cloud Infrastructure, Gallow Cloud Platform, Vetrix Cloud, Postrim Cloud, Openvale Cloud</p></div>
  <div class="card" style="left:380px"><div class="icon" role="img" aria-label="Illustrated icon of a light bulb and gear" style="background:linear-gradient(135deg,#fde7a8,#f4b46b)"></div><h3>CI/CD</h3><p>Collect &amp; Plan Requirements, Fetch Code, Build App Mod-ules, Test Automation, Re-lease Versioning, Zero Downtime</p></div>
  <div class="card" style="left:611px"><div class="icon" role="img" aria-label="Illustrated icon of an operating system mascot" style="background:linear-gradient(135deg,#f7c3bc,#e06a5a)"></div><h3>Linux Fundamentals</h3><p>Nimbara Linux/Devlan/Umbra/<br>Alpin/Redmark/Centra, Shell Scripting, Firewalls, Networking,</p></div>
  <div class="card" style="left:842px"><div class="icon" role="img" aria-label="Illustrated icon of a monitor with a gear" style="background:linear-gradient(135deg,#d6dbe6,#8fa0bd)"></div><h3>Monitoring</h3><p>NWS SkyWatch, Metricor, Dashwell, Searchly/Lensa, Logbit, Pollix, Tracewell</p></div>

  <div class="arrow" style="left:69px"><svg width="10" height="10" viewBox="0 0 10 10"><path d="M6.5 1.5L3 5l3.5 3.5" fill="none" stroke="#222" stroke-width="1.6"/></svg></div>
  <div class="arrow" style="left:1084px"><svg width="10" height="10" viewBox="0 0 10 10"><path d="M3.5 1.5L7 5 3.5 8.5" fill="none" stroke="#222" stroke-width="1.6"/></svg></div>

  <div class="abs" role="img" aria-label="Video still of the consultant speaking on stage at an investor conference in front of a seated audience" style="left:146px;top:2202px;width:909px;height:395px;background:linear-gradient(180deg,#4e4a4a 0%,#6b4a43 40%,#2a2222 75%,#141212 100%)"></div>
  <svg class="abs" style="left:568px;top:2366px" width="66" height="66" viewBox="0 0 66 66">
    <circle cx="33" cy="33" r="30" fill="none" stroke="#fff" stroke-width="4"/>
    <path d="M26 20l20 13-20 13z" fill="#fff"/>
  </svg>

  <div class="abs" style="left:149px;top:2729px;width:48px;height:1px;background:var(--red)"></div>
  <div class="abs" style="left:210px;top:2718px;font-size:13.5px;color:var(--red)">Check what People have to say.</div>
  <h2 class="abs serif" style="left:149px;top:2752px;font-size:32px">Testimonials</h2>
  <div class="abs serif" style="left:98px;top:2782px;font-size:110px;line-height:1;color:#e6e6e6">“</div>
  <p class="abs" style="left:155px;top:2828px;width:555px;font-size:12px;line-height:24.3px;color:var(--muted)">Marek helped us greatly in rolling out our productive clouds, when we needed compe-tent help. He has proven himself not only as very knowledgeable DevOps engineer in the area of NWS infrastructure and orkestra installation and deployments, but also with his great knowledge and experience in development. He has proven himself a very quick learner, who dived very fast in our project architecture.I would gladly recommend Marek as he is very dedicated person, who was spending plenty of weekends to help us</p>
  <div class="abs" role="img" aria-label="Portrait photo of the reviewer" style="left:154px;top:2992px;width:48px;height:48px;border-radius:50%;background:linear-gradient(135deg,#c9b9ad,#6f5f58)"></div>
  <div class="abs" style="left:221px;top:3005px;width:28px;height:1px;background:#444"></div>
  <div class="abs" style="left:256px;top:2995px;font-size:12.5px;font-weight:600;color:var(--ink)">Tomas Verhal</div>
  <div class="abs" style="left:219px;top:3020px;font-size:12.5px;color:var(--muted)">Senior Software Architect at Northgate Systems</div>
  <div class="abs" style="left:631px;top:3028px;display:flex;gap:12px">
    <span style="width:5px;height:5px;border-radius:50%;background:#999"></span>
    <span style="width:5px;height:5px;border-radius:50%;background:#999"></span>
    <span style="width:5px;height:5px;border-radius:50%;background:var(--red)"></span>
    <span style="width:5px;height:5px;border-radius:50%;background:#999"></span>
  </div>
  <div class="abs" role="img" aria-label="Illustration of two people leaving star ratings on a large tablet surrounded by plants" style="left:745px;top:2700px;width:435px;height:395px;border-radius:24px;background:linear-gradient(160deg,#eef3fb 0%,#dbe4f6 50%,#f8e1e1 100%)"></div>

  <section class="abs" style="left:0;top:3099px;width:1200px;height:447px;background:var(--grey-bg)"></section>
  <h2 class="section-title serif" style="top:3150px">Blogs</h2>
  <div class="blog">
    <div class="blog-img" role="img" aria-label="Illustration of a glowing cloud above server racks" style="left:156px;background:linear-gradient(135deg,#1f4fd8,#1aa3e8 60%,#6fd0ff)"></div>
    <h4 style="left:156px">Become Who You Say You Always Will</h4>
    <p style="left:156px">If I have a chance to whisper the best advice to a baby and he'll remember it for the rest of his life is this</p>
  </div>
  <div class="blog">
    <div class="blog-img" role="img" aria-label="Photograph of a keyboard, coffee cup and notebook on a desk" style="left:461px;background:linear-gradient(135deg,#4a4846,#8e877e 55%,#d8d0c4)"></div>
    <h4 style="left:461px">Explore Lakeview Mountain</h4>
    <p style="left:461px">If I have a chance to whisper the best advice to a baby and he'll remember it for the rest of his life is this</p>
  </div>
  <div class="blog">
    <div class="blog-img" role="img" aria-label="Photograph of a laptop showing a web page on a desk" style="left:764px;background:linear-gradient(135deg,#3e3c3b,#b7b2aa 50%,#e6e3de)"></div>
    <h4 style="left:764px">Cloud computing stratigies</h4>
    <p style="left:764px">If I have a chance to whisper the best advice to a baby and he'll remember it for the rest of his life is this</p>
  </div>

  <footer class="abs" style="left:0;top:3546px;width:1200px;height:380px;background:var(--footer)">
    <div class="logo" style="left:0;width:1200px;text-align:center;top:66px">Marekdovlin</div>
    <p class="abs" style="left:0;width:1200px;top:118px;text-align:center;font-size:14px;line-height:26px;color:#8f8f8f">I'm open for remote long and short-term<br>contracts and jobs. Connect with me:</p>
    <div class="btn" style="left:146px;top:213px;width:157px;height:37px;background:var(--navy);font-size:11px"><svg><use href="#download"/></svg>DOWNLOAD CV</div>
    <div class="btn" style="left:326px;top:213px;width:156px;height:37px;background:var(--sky)"><svg><use href="#send"/></svg>Start a chat</div>
    <div class="btn" style="left:505px;top:213px;width:183px;height:37px;background:var(--red)"><svg><use href="#mail"/></svg>Send a request</div>
    <div class="btn" style="left:711px;top:213px;width:157px;height:37px;background:var(--sky)"><span class="dot"></span>Start a chat</div>
    <div class="btn" style="left:898px;top:213px;width:157px;height:37px;background:var(--green)"><span class="dot"></span>marekdovlin</div>
    <div class="abs" style="left:146px;top:322px;display:flex;gap:14px;align-items:center;font-size:11px;color:#bdbdbd">
      <span style="display:flex;align-items:center;gap:5px"><span style="width:22px;height:22px;border-radius:50%;background:#3b5ea8"></span>Socialo</span>
      <span style="display:flex;align-items:center;gap:5px"><span style="width:22px;height:22px;border-radius:50%;background:#5a5a5a"></span>Pictura</span>
      <span style="display:flex;align-items:center;gap:5px"><span style="width:22px;height:22px;border-radius:50%;background:#1d78b6"></span>Worknet</span>
      <span style="display:flex;align-items:center;gap:5px"><span style="width:22px;height:22px;border-radius:50%;background:#1aa3e8"></span>Chirpa</span>
    </div>
    <div class="abs" style="right:139px;top:326px;font-size:11.5px;color:#4d4d4d">copyrights @ brevantu.cc All Rights Reserved</div>
  </footer>

</main>
</body>
</html>
```